construction co.logo(ie.highway,heavy equip)

need a design for a new construction company in washington state,office is located on the water (beach front)also use a 1952 dunmore keel avalis as portable office,or the standard bold construction type logo's,these are just thoughts and not necassarily direction

Target Market(s)

I will be working as a sub to much larger general contractors and am looking for a strong,stable appearance.

Industry/Entity Type

Construction

```html
<!DOCTYPE html>
<html lang="en">
<head>
<meta charset="utf-8">
<title>North Shore General Contractors – Business Card</title>
<link rel="stylesheet" href="https://fonts.googleapis.com/css2?family=Ubuntu:wght@300;400;500&display=swap">
<style>
  :root {
    --canvas: #ffffff;
    --slate: #3b4240;
    --slate-deep: #353b39;
    --slate-light: #56625f;
    --paper: #ffffff;
    --accent: #c8cc78;
    --edge: #333333;
  }
  * { box-sizing: border-box; margin: 0; padding: 0; }
  html, body {
    width: 1200px;
    height: 900px;
    overflow: hidden;
    background: var(--canvas);
    font-family: "Ubuntu", sans-serif;
  }
  .canvas { position: relative; width: 1200px; height: 900px; }

  .card {
    position: absolute;
    left: 340px;
    width: 598px;
    height: 386px;
    border: 1px solid var(--edge);
    overflow: hidden;
  }
  .card--front { top: 34px; background: var(--paper); }
  .card--back  { top: 484px; background: var(--slate-deep); }

  .card__art { position: absolute; inset: 0; width: 100%; height: 100%; }

  .brand { position: absolute; line-height: 1; }
  .brand__name { display: block; font-weight: 400; letter-spacing: -1px; }
  .brand__tagline { display: block; font-weight: 400; }
  .brand__square { position: absolute; }

  .card--front .brand { left: 334px; top: 232px; color: var(--slate); }
  .card--front .brand__name { font-size: 46px; }
  .card--front .brand__tagline { font-size: 23px; margin-top: 2px; letter-spacing: 0.2px; }
  .card--front .brand__square {
    width: 42px; height: 42px; right: -8px; top: -54px; background: var(--slate);
  }

  .card--back .brand { left: 32px; top: 76px; color: var(--paper); }
  .card--back .brand__name { font-size: 34px; }
  .card--back .brand__tagline { font-size: 17px; margin-top: 1px; }
  .card--back .brand__square {
    width: 30px; height: 30px; right: 0; top: -44px; background: var(--paper);
  }

  .contact-person { position: absolute; left: 32px; top: 178px; }
  .contact-person__name { font-size: 31px; font-weight: 300; color: var(--paper); line-height: 1.1; }
  .contact-person__role { font-size: 22px; font-weight: 300; color: var(--accent); line-height: 1.2; }

  .contact-list {
    position: absolute; left: 32px; top: 264px;
    list-style: none;
    font-size: 22px; font-weight: 300; color: var(--accent); line-height: 28px;
  }
</style>
</head>
<body>
<main class="canvas">

  <section class="card card--front" aria-label="Business card front">
    <svg class="card__art" viewBox="0 0 598 386" aria-hidden="false">
      <defs>
        <clipPath id="dark-panel">
          <polygon points="0,0 486,0 210,386 0,386"/>
        </clipPath>
        <linearGradient id="machine-tone" x1="0" y1="0" x2="1" y2="1">
          <stop offset="0" stop-color="#5d6966"/>
          <stop offset="1" stop-color="#4c5654"/>
        </linearGradient>
      </defs>
      <polygon points="0,0 486,0 210,386 0,386" fill="var(--slate)"/>
      <g clip-path="url(#dark-panel)">
        <rect x="40" y="0" width="300" height="386" fill="url(#machine-tone)" opacity="0.55"
              role="img" aria-label="Silhouette of an excavator arm and bucket"/>
      </g>
    </svg>
    <div class="brand">
      <span class="brand__square"></span>
      <span class="brand__name">North Shore</span>
      <span class="brand__tagline">general contractors</span>
    </div>
  </section>

  <section class="card card--back" aria-label="Business card back">
    <svg class="card__art" viewBox="0 0 598 386" aria-hidden="true">
      <polygon points="598,256 598,386 520,386" fill="var(--paper)"/>
    </svg>
    <div class="brand">
      <span class="brand__square"></span>
      <span class="brand__name">North Shore</span>
      <span class="brand__tagline">general contractors</span>
    </div>
    <div class="contact-person">
      <p class="contact-person__name">Dale Merritt</p>
      <p class="contact-person__role">Owner</p>
    </div>
    <ul class="contact-list">
      <li>northshorecontractors@mailbox.com</li>
      <li>360-555-0142</li>
      <li>48 cove ln port ellis wa 98000</li>
    </ul>
  </section>

</main>
</body>
</html>
```